Save The Date for 2019 QRP Symposium

We have an annual meeting each June and need a Save the Date (STD) designed. It should be a two-sided postcard with room for address and stamp (according to US Mail postal standards). I have attached some examples from prior years, but we would appreciate a more modern and attractive design for this year's STD.

Target Market(s)

Our own members - nurses, nurse practitioners, PAs and physicians

Industry/Entity Type

Medical

Requirements
Must have
• Must include our logos (attached), ideally in a coordinating fashion - as was done in prior years (see examples attached) and without modifying the logos too much. Needs have the following information:
• - "Save the Date"
• - "The 12th Annual Vascular Crew Roundtable"
• - "Friday, June 7, 2019" or "6/7/19"
• - "The Halvern–Trask Building | 274 West 19th Street | NYC"
• - Please include our website (www.zq-olm.example/events), phone number (212-555-0147) and email address (ask@zq-olm.example) for people to ask questions
• - Must have space for a postage stamp and the name/address of the postcard recipient
Nice to have
• Would be nice to remain in our blue/grey/olive color palate (see attached Brand Standards guide).
Should not have
• Please do not use stock photos of medical staff. Please don't use cartoons or cartoon images (although a tasteful sketch may be considered).

```html
<!DOCTYPE html>
<html lang="en">
<head>
<meta charset="utf-8">
<title>Save the Date – 12th Annual Vascular Crew Roundtable</title>
<link href="https://fonts.googleapis.com/css2?family=Nunito+Sans:wght@400;600;800&display=swap" rel="stylesheet">
<style>
  :root {
    --page: #ffffff;
    --navy-deep: #0b2557;
    --navy-mid: #1a4380;
    --rule: #6f8fbf;
    --ink-light: #ffffff;
    --ink-soft: #dfe7f3;
    --heart-red: #e8283f;
    --heart-rose: #f0546a;
  }
  * { margin: 0; padding: 0; box-sizing: border-box; }
  html, body {
    width: 1200px;
    height: 927px;
    overflow: hidden;
    background: var(--page);
    font-family: "Nunito Sans", Arial, sans-serif;
  }
  .canvas { position: relative; width: 1200px; height: 927px; }

  .postcard {
    position: absolute;
    width: 546px;
    height: 422px;
    background: radial-gradient(ellipse at 55% 45%, var(--navy-mid) 0%, var(--navy-deep) 75%);
    color: var(--ink-light);
    overflow: hidden;
  }
  .postcard--front { left: 310px; top: 28px; }
  .postcard--back  { left: 312px; top: 463px; }

  .card-header { position: absolute; left: 0; top: 0; width: 100%; height: 120px; }
  .brand { position: absolute; left: 16px; top: 22px; display: flex; align-items: center; gap: 14px; }
  .brand__dot {
    width: 64px; height: 64px; border-radius: 50%;
    border: 3px solid var(--ink-light);
  }
  .brand__name {
    font-size: 22px; font-weight: 600; color: var(--ink-light);
    line-height: 1.1; width: 190px;
  }
  .partner-badge {
    position: absolute; top: 20px;
    width: 56px; height: 56px; border-radius: 50%;
    background: var(--ink-light);
  }
  .partner-badge--one { left: 403px; }
  .partner-badge--two { left: 470px; }
  .header-rule {
    position: absolute; left: 0; top: 92px; width: 390px; height: 1px;
    background: var(--rule);
  }

  .illustration-slot {
    position: absolute; left: 0; top: 122px; width: 347px; height: 138px;
    background: linear-gradient(90deg, var(--ink-soft) 0%, var(--heart-rose) 60%, var(--heart-red) 100%);
    border-radius: 0 70px 70px 0;
    opacity: 0.95;
  }

  .headline {
    position: absolute; right: 29px; top: 292px; text-align: left; width: 260px;
  }
  .headline__title {
    font-size: 31px; font-weight: 800; letter-spacing: 0.5px; line-height: 1.1;
  }
  .headline__event {
    margin-top: 8px; font-size: 17px; font-weight: 400; line-height: 1.22;
    text-transform: uppercase; letter-spacing: 0.3px;
  }
  .headline__event sup { font-size: 10px; }

  .address-block { position: absolute; left: 30px; top: 177px; width: 207px; }
  .address-block__line { height: 1px; background: var(--rule); margin-bottom: 25.5px; }

  .event-details { position: absolute; left: 346px; top: 208px; font-size: 17px; line-height: 1.25; }
  .event-details__date { font-weight: 800; font-size: 18px; }

  .contact-line {
    position: absolute; left: 0; top: 385px; width: 100%;
    text-align: center; font-size: 10.5px; color: var(--ink-soft);
  }
</style>
</head>
<body>
<main class="canvas">

  <section class="postcard postcard--front" aria-label="Postcard front">
    <header class="card-header">
      <div class="brand">
        <span class="brand__dot"></span>
        <span class="brand__name">Meridian Vascular College</span>
      </div>
      <span class="partner-badge partner-badge--one"></span>
      <span class="partner-badge partner-badge--two"></span>
      <span class="header-rule"></span>
    </header>

    <div class="illustration-slot" role="img" aria-label="Illustration of a gloved hand in a white sleeve holding a red heart crossed by a heartbeat line"></div>

    <div class="headline">
      <h1 class="headline__title">SAVE THE DATE</h1>
      <p class="headline__event">12<sup>th</sup> Annual Vascular<br>Crew Roundtable</p>
    </div>
  </section>

  <section class="postcard postcard--back" aria-label="Postcard back">
    <header class="card-header">
      <div class="brand">
        <span class="brand__dot"></span>
        <span class="brand__name">Meridian Vascular College</span>
      </div>
      <span class="partner-badge partner-badge--one"></span>
      <span class="partner-badge partner-badge--two"></span>
      <span class="header-rule"></span>
    </header>

    <div class="address-block" aria-label="Recipient address lines">
      <div class="address-block__line"></div>
      <div class="address-block__line"></div>
      <div class="address-block__line"></div>
      <div class="address-block__line"></div>
      <div class="address-block__line"></div>
      <div class="address-block__line"></div>
    </div>

    <div class="event-details">
      <p class="event-details__date">Friday, June 7, 2019</p>
      <p>The Halvern–Trask Building</p>
      <p>274 West 19th Street</p>
    </div>

    <p class="contact-line">For additional information call 212-555-0147 or email ask@zq-olm.example or visit www.zq-olm.example/events</p>
  </section>

</main>
</body>
</html>
```